Occupational Therapist does home accessibility for disabled folks; needs business card design

We need a business card for a company in Portland, Oregon that specializes in making homes accessible, comfortable, and functional for people who are disabled or aging who would like to stay in THEIR home. Our medical background as Occupational Therapists allows us to translate the functional needs of the person into the recommendations for the design of the home remodel.

Target Market(s)

Elderly, children of elderly
People with disabilities, families of people with disabilities

Industry/Entity Type

Business

Contact Information for Business Card

Company name: HomeWell
Name: Karen Dwyer Lopez, OTR/L, CAPS, ECHM
Occupational Therapist, Home Modification & Accessibility Specialist
website: www.homewellsteady.com
email: homewellsteady@mailbright.com
phone: (503)418-2957
CCB #: 384517

Font styles to use
Sans Serif

Requirements
Must have
• My logo
• Easy to read font with contrasting background
• Please list the Services offered: Occupational Therapy, Home safety & accessibility assessments, Home modification consulting, project management
Nice to have
• Friendly, welcoming feel
Should not have
• Dark colored background

```html
<!DOCTYPE html>
<html lang="en">
<head>
<meta charset="utf-8">
<title>Hearthmoor Business Card</title>
<link rel="stylesheet" href="https://fonts.googleapis.com/css2?family=Source+Sans+3:wght@400;500;600&display=swap">
<style>
  :root {
    --stage: #c9c9c9;
    --card: #ffffff;
    --band: #6f6f6f;
    --orange: #d4822f;
    --ink-light: #ffffff;
    --ink-name: #666666;
    --ink-dark: #2b2b2b;
  }
  * { margin: 0; padding: 0; box-sizing: border-box; }
  html, body {
    width: 1189px; height: 1200px; overflow: hidden;
    background: var(--stage);
    font-family: "Source Sans 3", sans-serif;
  }
  .card {
    position: absolute; left: 194px;
    width: 808px; height: 461px;
    background: var(--card);
    overflow: hidden;
  }
  .card--front { top: 111px; }
  .card--back { top: 620px; }

  .brand {
    position: absolute; left: 0; right: 0;
    display: flex; align-items: center; justify-content: center; gap: 16px;
    color: var(--orange); font-weight: 600; line-height: 1;
  }
  .brand__mark { width: 0.55em; height: 0.55em; background: var(--orange); }
  .card--front .brand { top: 76px; font-size: 74px; }
  .card--back .brand { top: 132px; font-size: 92px; }

  .band {
    position: absolute; left: 0; right: 0; top: 196px; bottom: 0;
    background: var(--band);
  }
  .contact {
    position: absolute; left: 48px; top: 92px;
    list-style: none; color: var(--ink-light); font-size: 21px;
  }
  .contact li { display: flex; align-items: center; height: 32.5px; white-space: nowrap; }
  .contact svg { width: 20px; height: 20px; margin-right: 17px; flex: none; }
  .role {
    position: absolute; right: 48px; top: 120px;
    text-align: right; color: var(--ink-light);
    font-size: 20px; font-weight: 500; line-height: 27px;
  }

  .holder { position: absolute; left: 0; right: 0; top: 332px; text-align: center; }
  .holder__name { font-size: 30px; color: var(--ink-name); line-height: 38px; }
  .holder__creds { font-size: 20px; color: var(--ink-dark); line-height: 24px; }
  .tab { position: absolute; top: 322px; width: 35px; height: 97px; background: var(--band); }
  .tab--left { left: 0; }
  .tab--right { right: 0; }
</style>
</head>
<body>
  <section class="card card--front">
    <div class="brand"><span class="brand__mark"></span>Hearthmoor</div>
    <div class="band">
      <ul class="contact">
        <li>
          <svg viewBox="0 0 20 20" aria-hidden="true"><rect width="20" height="20" fill="#fff"/><path d="M6 4l3 3-1.5 2c1 2 2 3 4 4l2-1.5 3 3-2 2C8 16 4 12 4 6z" fill="#6f6f6f"/></svg>
          (503)418-2957
        </li>
        <li>
          <svg viewBox="0 0 20 20" aria-hidden="true"><rect width="20" height="20" fill="#fff"/><circle cx="10" cy="10" r="6.5" fill="none" stroke="#6f6f6f" stroke-width="1.6"/><path d="M3.5 10h13M10 3.5c-3 3-3 10 0 13M10 3.5c3 3 3 10 0 13" fill="none" stroke="#6f6f6f" stroke-width="1.2"/></svg>
          www.hearthmoorliving.com
        </li>
        <li>
          <svg viewBox="0 0 20 20" aria-hidden="true"><rect width="20" height="20" fill="#fff"/><rect x="3" y="5.5" width="14" height="9" fill="none" stroke="#6f6f6f" stroke-width="1.4"/><path d="M3 5.5l7 5 7-5" fill="none" stroke="#6f6f6f" stroke-width="1.4"/></svg>
          hearthmoorliving@mailbright.com
        </li>
        <li>CCB #: 384517</li>
      </ul>
      <p class="role">Occupational Therapist, Home<br>Modification &amp; Accessibility Specialist</p>
    </div>
  </section>

  <section class="card card--back">
    <div class="brand"><span class="brand__mark"></span>Hearthmoor</div>
    <div class="tab tab--left"></div>
    <div class="tab tab--right"></div>
    <div class="holder">
      <p class="holder__name">Karen Dwyer Lopez</p>
      <p class="holder__creds">OTR/L, CAPS, ECHM</p>
    </div>
  </section>
</body>
</html>
```